Redesign current business card for food company

i would like to redesign my business card. our company is food company, our product range from chips, juices, milk and etc (mostly dried food stuff).
I want o keep same logo but , the rest is open to new design.
you can check at our website about our company www.torvikeats.com

Target Market(s)

most of food company

Industry/Entity Type

Business

Contact Information for Business Card

I want to keep more to blue color...

Colors
3176b5
abd036

Requirements
Must have
• our old logo
Nice to have
• we do not mind to have nice material on bus card in order to accomplish nice design. for example: using spot uv, embossed and etc.

```html
<!DOCTYPE html>
<html lang="en">
<head>
<meta charset="utf-8">
<title>Torvik Enterprises – Business Card</title>
<link rel="stylesheet" href="https://fonts.googleapis.com/css2?family=Questrial&family=Open+Sans:wght@400;600;700&display=swap">
<style>
  :root {
    --page: #e9edf2;
    --card-blue: #0b45f2;
    --back-start: #0a48f4;
    --back-end: #1ea3f2;
    --accent-dark: #0b0d55;
    --accent-mid: #1d4aa5;
    --accent-light: #00a6e6;
    --white: #ffffff;
    --icon-ink: #1456c8;
  }
  * { margin: 0; padding: 0; box-sizing: border-box; }
  html, body { width: 1200px; height: 1200px; overflow: hidden; background: var(--page); }
  .canvas {
    width: 1200px; height: 1200px;
    display: flex; flex-direction: column; align-items: center; justify-content: center; gap: 40px;
  }
  .card {
    position: relative; width: 960px; height: 548px; overflow: hidden;
    box-shadow: 0 10px 28px rgba(10, 30, 80, 0.22);
  }
  /* Front: contact side */
  .card--contact { background: var(--card-blue); }
  .accent-area { position: absolute; left: 0; top: 0; }
  .identity {
    position: absolute; right: 60px; top: 54px; text-align: right; color: var(--white);
    font-family: "Questrial", sans-serif;
  }
  .identity__name { font-size: 62px; line-height: 1; letter-spacing: -0.5px; white-space: nowrap; }
  .identity__title { font-size: 32px; margin-top: 6px; }
  .company {
    position: absolute; right: 60px; top: 214px; color: var(--white);
    font-family: "Open Sans", sans-serif; font-weight: 700; font-size: 32px;
    border-bottom: 2px solid var(--white); padding-bottom: 2px; line-height: 1.15; white-space: nowrap;
  }
  .contact-list {
    position: absolute; left: 500px; top: 290px; list-style: none;
    font-family: "Open Sans", sans-serif; font-size: 19px; color: var(--white);
  }
  .contact-list li { display: flex; align-items: center; gap: 24px; height: 38px; white-space: nowrap; }
  .contact-icon { width: 32px; height: 32px; flex: none; }
  .contact-icon rect.badge { fill: var(--white); }
  .contact-icon .glyph { fill: none; stroke: var(--icon-ink); stroke-width: 1.8; stroke-linejoin: round; stroke-linecap: round; }
  .contact-icon .glyph-fill { fill: var(--icon-ink); }
  /* Back: brand side */
  .card--brand {
    background: linear-gradient(135deg, var(--back-start) 0%, var(--back-start) 30%, var(--back-end) 100%);
    display: flex; align-items: center; justify-content: center;
  }
  .brand-name {
    font-family: "Open Sans", sans-serif; font-weight: 700; font-size: 230px;
    color: var(--white); letter-spacing: -6px; line-height: 1;
  }
</style>
</head>
<body>
<main class="canvas">
  <section class="card card--contact">
    <svg class="accent-area" width="480" height="548" viewBox="0 0 480 548" role="img" aria-label="Decorative layered chevron pattern in navy and cyan blues">
      <defs>
        <linearGradient id="accentTone" x1="0" y1="0.5" x2="1" y2="0.5">
          <stop offset="0" stop-color="var(--accent-dark)"/>
          <stop offset="0.5" stop-color="var(--accent-mid)"/>
          <stop offset="1" stop-color="var(--accent-light)"/>
        </linearGradient>
      </defs>
      <polygon fill="url(#accentTone)" points="0,0 260,0 460,290 300,548 0,548"/>
    </svg>

    <div class="identity">
      <p class="identity__name">Marcus Delvane</p>
      <p class="identity__title">President</p>
    </div>
    <p class="company">Torvik Enterprises Corp.</p>

    <ul class="contact-list">
      <li>
        <svg class="contact-icon" viewBox="0 0 32 32" aria-hidden="true"><rect class="badge" width="32" height="32" rx="7"/><path class="glyph" d="M7 16 L16 8 L25 16 M10 14 V24 H22 V14 M14 24 V18 H18 V24"/></svg>
        418 E Harlow Ave. Riverton CA 90412
      </li>
      <li>
        <svg class="contact-icon" viewBox="0 0 32 32" aria-hidden="true"><rect class="badge" width="32" height="32" rx="7"/><path class="glyph" d="M7 13 Q16 6 25 13 L23 15 L19 13 V11 H13 V13 L9 15 Z"/><rect class="glyph" x="9" y="16" width="14" height="8" rx="2"/><circle class="glyph" cx="16" cy="20" r="2"/></svg>
        555-201-3340
      </li>
      <li>
        <svg class="contact-icon" viewBox="0 0 32 32" aria-hidden="true"><rect class="badge" width="32" height="32" rx="7"/><rect class="glyph" x="9" y="6" width="14" height="12"/><path class="glyph" d="M11 10 H21 M11 13 H21"/><rect class="glyph-fill" x="7" y="19" width="18" height="7" rx="1.5"/></svg>
        555-201-3341
      </li>
      <li>
        <svg class="contact-icon" viewBox="0 0 32 32" aria-hidden="true"><rect class="badge" width="32" height="32" rx="7"/><rect class="glyph" x="11" y="7" width="10" height="19" rx="2"/><rect class="glyph" x="13" y="10" width="6" height="5"/><path class="glyph" d="M13 19 H19 M13 22 H19"/></svg>
        555-384-7712
      </li>
      <li>
        <svg class="contact-icon" viewBox="0 0 32 32" aria-hidden="true"><rect class="badge" width="32" height="32" rx="7"/><rect class="glyph" x="7" y="10" width="18" height="13"/><path class="glyph" d="M7 10 L16 18 L25 10 M7 23 L13 16 M25 23 L19 16"/></svg>
        Marcus@torvikeats.com
      </li>
      <li>
        <svg class="contact-icon" viewBox="0 0 32 32" aria-hidden="true"><rect class="badge" width="32" height="32" rx="7"/><circle class="glyph" cx="16" cy="16" r="9"/><ellipse class="glyph" cx="16" cy="16" rx="4" ry="9"/><path class="glyph" d="M7 16 H25 M9 11 H23 M9 21 H23"/></svg>
        www.torvikeats.com
      </li>
    </ul>
  </section>

  <section class="card card--brand">
    <p class="brand-name">torvik</p>
  </section>
</main>
</body>
</html>
```